Marketing Flyer for Ashford Ridge Storage Climate Control Units

We are looking for a professional looking Marketing Flyer to advertise for our Climate Control Self Storage Units. Incorporate photos and our LOGO into the marketing flyer. See our website: AshfordRidgestorage.example
Updates

Marketing Flyer for our Self Storage Climate Control Units at Ashford Ridge Storage in Waynesville, NC

Want more designers to have a chance to submit entries.

Target Market(s)

Self Storage Facility Renters

Industry/Entity Type

Self Storage Facility

Font styles to use
Other font styles liked:
• Montserrat Font is what was used for our LOGO and would like to maintain consistency of Font on the Flyer

Colors
0054AA
0677BA
7BADD7
CADEEF
E8F1F8

Requirements
Must have
• Need to have LOGO in the Flyer and photos of the Climate Control Units

```html
<!DOCTYPE html>
<html lang="en">
<head>
<meta charset="utf-8">
<title>Ashford Ridge Storage – Climate Control Flyer</title>
<link rel="stylesheet" href="https://fonts.googleapis.com/css2?family=Montserrat:ital,wght@0,300;0,400;0,500;0,700;0,800;0,900;1,600&display=swap">
<style>
  :root {
    --navy: #1b1a5e;
    --navy-deep: #15144d;
    --brand-blue: #0677BA;
    --brand-dark: #0054AA;
    --sky: #7BADD7;
    --mist: #CADEEF;
    --ice: #E8F1F8;
    --white: #ffffff;
    --ink: #1e1e3c;
  }
  * { box-sizing: border-box; margin: 0; padding: 0; }
  html, body { width: 742px; height: 1200px; overflow: hidden; background: var(--white); }
  body { font-family: "Montserrat", sans-serif; }
  .flyer { position: relative; width: 742px; height: 1200px; overflow: hidden; }
  .flyer-shapes { position: absolute; inset: 0; width: 742px; height: 1200px; }
  .abs { position: absolute; }

  .headline {
    left: 251px; top: 332px;
    color: var(--white); font-weight: 800; font-size: 48px; line-height: 51px;
    text-transform: uppercase; white-space: nowrap;
  }

  .unit { color: var(--white); }
  .unit-size { font-weight: 700; font-size: 46px; line-height: 52px; }
  .unit-label { font-weight: 400; font-size: 19px; letter-spacing: 0.5px; margin-top: 6px; }
  .unit-divider { width: 1.5px; background: var(--brand-blue); }

  .features {
    left: 32px; top: 1048px; width: 336px; height: 119px;
    border: 1.5px solid var(--brand-blue); border-radius: 12px;
  }
  .feature { color: var(--white); text-align: center; font-size: 18px; line-height: 20px; }
  .feature svg { display: block; margin: 0 auto 14px; }

  .padlock-photo {
    left: 330px; top: 861px; width: 90px; height: 339px;
    background: linear-gradient(180deg, var(--sky) 0%, var(--brand-dark) 40%, #2a4aa0 60%, #b9b9b0 75%, #8c8a7e 100%);
    border-radius: 40px 40px 6px 6px;
  }

  .brand-mark {
    left: 536px; top: 648px; width: 68px; height: 68px;
    border-radius: 50%; background: var(--navy);
  }
  .brand-name {
    left: 420px; top: 748px; width: 300px; text-align: center;
    color: var(--navy); font-weight: 700; font-size: 22px; line-height: 27px; letter-spacing: 0.3px;
  }

  .review { left: 450px; top: 836px; width: 270px; color: var(--ink); }
  .reviewer { font-style: italic; font-weight: 600; font-size: 15px; }
  .stars { color: var(--brand-blue); font-size: 17px; letter-spacing: 6px; margin-left: 8px; }
  .review-text { margin-top: 10px; font-size: 14.5px; line-height: 21px; font-weight: 400; white-space: nowrap; }

  .address { left: 457px; top: 978px; color: var(--ink); font-size: 18px; line-height: 24px; display: flex; gap: 9px; }
  .address svg { flex: none; margin-top: 2px; }

  .phone-box {
    left: 399px; top: 1047px; width: 311px; height: 120px;
    background: var(--brand-blue); border-radius: 16px;
    display: flex; align-items: center; justify-content: flex-end; padding-right: 26px; gap: 10px;
    color: var(--white); font-weight: 700; font-size: 27px;
  }
</style>
</head>
<body>
<main class="flyer">
  <svg class="flyer-shapes" viewBox="0 0 880 1245" preserveAspectRatio="none">
    <defs>
      <linearGradient id="corridor-tones" x1="0" y1="0" x2="1" y2="0">
        <stop offset="0" stop-color="#27348a"/>
        <stop offset="0.25" stop-color="#5a6ab0"/>
        <stop offset="0.5" stop-color="#d6dbe4"/>
        <stop offset="0.75" stop-color="#5a6ab0"/>
        <stop offset="1" stop-color="#27348a"/>
      </linearGradient>
      <linearGradient id="navy-panel" x1="0" y1="0" x2="0" y2="1">
        <stop offset="0" stop-color="#2e2c7a"/>
        <stop offset="0.35" stop-color="#1b1a5e"/>
        <stop offset="1" stop-color="#15144d"/>
      </linearGradient>
      <clipPath id="lower-half"><rect x="0" y="560" width="880" height="300"/></clipPath>
    </defs>
    <rect role="img" aria-label="Photo of an indoor corridor lined with blue roll-up storage unit doors" x="0" y="0" width="880" height="740" fill="url(#corridor-tones)"/>
    <polygon points="0,477 440,720 440,1245 0,1245" fill="url(#navy-panel)"/>
    <polygon points="880,470 440,720 440,1245 880,1245" fill="#ffffff"/>
    <polyline points="0,472 440,716 880,466" fill="none" stroke="#ffffff" stroke-width="12"/>
    <polyline points="443,729 880,484" fill="none" stroke="#1b1a5e" stroke-width="5"/>
    <path clip-path="url(#lower-half)" d="M440,266 L621,362 L621,608 L440,695 L253,608 L253,362 Z" fill="#ffffff" stroke="#ffffff" stroke-width="44" stroke-linejoin="round"/>
    <path d="M440,266 L621,362 L621,608 L440,695 L253,608 L253,362 Z" fill="#0677BA" stroke="#0677BA" stroke-width="24" stroke-linejoin="round"/>
  </svg>

  <h1 class="abs headline">Climate<br>Control<br>Self<br>Storage<br>Units</h1>

  <div class="abs unit" style="left:40px;top:700px"><div class="unit-size">5’<br>5’</div><div class="unit-label">SMALL</div></div>
  <div class="abs unit-divider" style="left:130px;top:706px;height:128px"></div>
  <div class="abs unit" style="left:152px;top:700px"><div class="unit-size">5’<br>10’</div><div class="unit-label">SMALL</div></div>
  <div class="abs unit-divider" style="left:243px;top:706px;height:128px"></div>
  <div class="abs unit" style="left:264px;top:700px"><div class="unit-size">10’<br>10’</div><div class="unit-label">SMALL</div></div>

  <div class="abs unit" style="left:72px;top:872px"><div class="unit-size">10’<br>12’</div><div class="unit-label">MEDIUM</div></div>
  <div class="abs unit-divider" style="left:187px;top:877px;height:126px"></div>
  <div class="abs unit" style="left:210px;top:872px"><div class="unit-size">10’<br>17’</div><div class="unit-label">MEDIUM</div></div>

  <div class="abs features">
    <div class="abs feature" style="left:50px;top:14px;width:68px">
      <svg width="30" height="30" viewBox="0 0 30 30" fill="none" stroke="#ffffff" stroke-width="1.8"><path d="M20 4H5v21h21V12"/><path d="M12 18l14-14M12 10v8h8"/></svg>
      Inside
    </div>
    <div class="abs feature" style="left:144px;top:10px;width:130px">
      <svg width="30" height="34" viewBox="0 0 30 34" fill="none" stroke="#ffffff" stroke-width="1.8"><path d="M12 4a3 3 0 016 0v17a6 6 0 11-6 0z"/><path d="M15 12v12"/><path d="M6 8h3M6 12h3M6 16h3M22 6q3 2 0 5M24 3q5 5 0 11"/></svg>
      Climate<br>Controlled
    </div>
  </div>

  <div class="abs phone-box">
    <svg width="22" height="22" viewBox="0 0 22 22"><circle cx="11" cy="11" r="11" fill="#ffffff"/><path d="M7.5 6l2 2-1 1.5q1 2.5 3.5 3.5l1.5-1 2 2-1.5 1.5Q9 15 6 8z" fill="none" stroke="#0677BA" stroke-width="1.3" stroke-linejoin="round"/></svg>
    (555) 010-4427
  </div>

  <div class="abs padlock-photo" role="img" aria-label="Photo of a blue branded padlock with a key"></div>

  <div class="abs brand-mark" aria-hidden="true"></div>
  <div class="abs brand-name">ASHFORD RIDGE<br>STORAGE</div>

  <div class="abs review">
    <div><span class="reviewer">mkellerman</span><span class="stars">★★★★★</span></div>
    <p class="review-text">Excellent service and wonderful<br>space to store all of my cool stuff!<br>Highly recommend!</p>
  </div>

  <div class="abs address">
    <svg width="20" height="20" viewBox="0 0 20 20"><circle cx="10" cy="10" r="9.5" fill="#0677BA"/><path d="M10 4.5a3.5 3.5 0 013.5 3.5c0 2.6-3.5 6.5-3.5 6.5S6.5 10.6 6.5 8A3.5 3.5 0 0110 4.5z" fill="none" stroke="#fff" stroke-width="1.2"/><circle cx="10" cy="8" r="1.2" fill="#fff"/></svg>
    <span>42 Alder Lane,<br>Millbrook, VT 05860</span>
  </div>
</main>
</body>
</html>
```